Bref créative
Business Cards/Stationary for a Consulting Company
Darvey Solutions
Simple
Lorette Darvey
PO BOX 4087
Sunridge, AZ 85099
lorette@darveysolutions-example.com
www.darveysolutions-example.com

```html
<!DOCTYPE html>
<html lang="en">
<head>
<meta charset="utf-8">
<title>Darvey Solutions — Business Card</title>
<link href="https://fonts.googleapis.com/css2?family=Tinos:wght@400;700&display=swap" rel="stylesheet">
<style>
  :root {
    --bg: #d9d9d9;
    --navy: #0d2a8a;
    --blue: #1565d8;
    --bright: #1f8ef0;
    --sky: #3aa6f5;
    --ink: #1f2a44;
    --grey: #5a6070;
    --rule: #c8ccd4;
    --paper: #ffffff;
  }
  html, body {
    margin: 0;
    width: 1200px;
    height: 871px;
    overflow: hidden;
    background: var(--bg);
    font-family: "Tinos", "Times New Roman", serif;
  }
  .canvas {
    position: relative;
    width: 1200px;
    height: 871px;
  }
  .card {
    position: absolute;
    left: 250px;
    width: 700px;
    height: 400px;
    overflow: hidden;
    box-shadow: 0 6px 18px rgba(0,0,0,0.22);
  }
  /* Back side */
  .card-back {
    top: 24px;
    background: linear-gradient(160deg, var(--navy) 0%, var(--blue) 45%, var(--sky) 100%);
    color: var(--paper);
  }
  .back-mark {
    position: absolute;
    left: 0; right: 0; top: 140px;
    display: flex;
    align-items: center;
    justify-content: center;
    gap: 20px;
  }
  .back-dot {
    width: 64px; height: 64px;
    border-radius: 50%;
    background: var(--paper);
  }
  .back-name {
    font-size: 40px;
    letter-spacing: 1px;
  }
  .back-url {
    position: absolute;
    left: 0; right: 0; bottom: 90px;
    text-align: center;
    font-size: 17px;
    letter-spacing: 2px;
    opacity: 0.92;
  }
  /* Front side */
  .card-front {
    top: 447px;
    background: linear-gradient(180deg, #ffffff 0%, #f3f4f6 100%);
  }
  .band-top {
    position: absolute; left: 0; right: 0; top: 0;
    height: 30px;
    background: linear-gradient(90deg, var(--bright) 0%, var(--blue) 55%, var(--navy) 100%);
  }
  .band-top::after {
    content: ""; position: absolute; left: 0; right: 0; bottom: -9px;
    height: 3px; background: var(--blue);
  }
  .band-bottom {
    position: absolute; left: 0; right: 0; bottom: 0;
    height: 66px;
    background: linear-gradient(90deg, var(--sky) 0%, var(--blue) 45%, var(--navy) 100%);
  }
  .band-bottom::before {
    content: ""; position: absolute; left: 0; right: 0; top: -10px;
    height: 3px; background: var(--navy);
  }
  .brand {
    position: absolute;
    left: 40px; top: 178px;
    display: flex; align-items: center; gap: 12px;
  }
  .brand-dot {
    width: 40px; height: 40px; border-radius: 50%;
    background: var(--navy);
  }
  .brand-name {
    font-size: 29px;
    color: var(--blue);
    font-weight: 700;
  }
  .divider {
    position: absolute;
    left: 330px; top: 62px; bottom: 96px;
    width: 1px; background: var(--rule);
  }
  .details {
    position: absolute;
    left: 350px; top: 72px;
    color: var(--ink);
  }
  .person-name {
    font-size: 24px;
    font-variant: small-caps;
    color: var(--navy);
    letter-spacing: 0.5px;
  }
  .person-title {
    font-size: 15px;
    color: var(--grey);
    margin-top: 2px;
  }
  .address {
    margin-top: 22px;
    font-size: 15px;
    line-height: 19px;
  }
  .contacts {
    list-style: none; margin: 16px 0 0; padding: 0;
    font-size: 14px; line-height: 20px;
  }
  .contacts li { display: flex; align-items: center; gap: 8px; white-space: nowrap; }
  .contacts svg { width: 11px; height: 11px; fill: var(--navy); flex: none; }
</style>
</head>
<body>
<main class="canvas">
  <section class="card card-back" aria-label="Card back">
    <div class="back-mark">
      <span class="back-dot"></span>
      <span class="back-name">Darvey Solutions</span>
    </div>
    <div class="back-url">www.darveysolutions-example.com</div>
  </section>

  <section class="card card-front" aria-label="Card front">
    <div class="band-top"></div>
    <div class="brand">
      <span class="brand-dot"></span>
      <span class="brand-name">Darvey Solutions</span>
    </div>
    <div class="divider"></div>
    <div class="details">
      <div class="person-name">Lorette Darvey</div>
      <div class="person-title">Managing Director</div>
      <div class="address">PO BOX 4087<br>Sunridge, AZ 85099</div>
      <ul class="contacts">
        <li><svg viewBox="0 0 12 12"><path d="M2.5 1 L4.5 1 L5.3 3.5 L4 4.6 C4.7 6 6 7.3 7.4 8 L8.5 6.7 L11 7.5 L11 9.5 C11 10.3 10.3 11 9.5 11 C5 11 1 7 1 2.5 C1 1.7 1.7 1 2.5 1 Z"/></svg>623-555-0148</li>
        <li><svg viewBox="0 0 12 12"><path d="M1 2.5 H11 V9.5 H1 Z M1.8 3.2 L6 6.4 L10.2 3.2 V8.8 H1.8 Z" fill-rule="evenodd"/></svg>lorette@darveysolutions-example.com</li>
        <li><svg viewBox="0 0 12 12"><circle cx="6" cy="6" r="5"/></svg>www.darveysolutions-example.com</li>
      </ul>
    </div>
    <div class="band-bottom"></div>
  </section>
</main>
</body>
</html>
```